Wordpress Identity for Innovation Firm

Copper Lantern Partners is an innovation and investment firm based in Los Angeles.

We are seeking a designer that can help create our company identity and Wordpress site.

The attached Design Brief provides more details.

Designers Responsibility:

1) Company Identity

The designer will create the company identity.
Attached is a file that contains a type font that I like a lot.
No logo design is required.

The Copper Lantern Partners type font should become the company identity.
The attached document provides an overview of company type font identities that we like.

2) Wordpress Theme & Design

The designer will select existing Wordpress Themes that meet our design desires, and present them as part of the design proposal.

We will make our selection based on the selected Wordpress Theme(s), which the designer will creatively adapt with the new company identity.

Target Market(s)

We anticipate the website being mostly accessed by the US, Canada and European countries.

Our target audience includes the following:

• Corporations, companies, startups, non-profits
• Banks, venture capital, private equity, investors
• Incubators, accelerators, innovation clusters, research labs, universities
• Ad agencies, marketing agencies, digital agencies, media, press

Industry/Entity Type

Investment

Number of Pages Required

1 page

Font styles to use
Sans Serif
Other font styles liked:
• See attached design brief materials. The Font will represent the brand identity!

Requirements
Must have
• The ability to scroll through information top to bottom is important to us.
• This is in line with today's Wordpress themes.
• The website must be able to function across devices (desktop, tablet, phone).
• The top 5 web browsers and platforms (Mac/PC/Android/iOS)
• Contact us link or information field
Nice to have
• It would be nice to have a moving image in the background, such as:
• https://drifttrial.sitehatch.com
• The Wordpress theme of the moving image or video should be relevant to our overall Technology Innovation theme.
• Key words:
• Technology Innovation
• Digital
• Business
• Transportation
• Advanced Vehicles (auto, boat, airplane, rail, space)
• Space
• Venture Capital
• Investing
Should not have
• eCommerce

```html
<!DOCTYPE html>
<html lang="en">
<head>
<meta charset="utf-8">
<title>Copper Lantern Partners</title>
<link href="https://fonts.googleapis.com/css2?family=Montserrat:wght@700&family=Open+Sans:wght@300;400;600;700&display=swap" rel="stylesheet">
<style>
  :root{
    --ink:#222;
    --text:#555;
    --muted:#888;
    --line:#d6d6d6;
    --dark:#2a2a2a;
    --darker:#1e1e1e;
    --white:#fff;
    --panel:#f1f1f1;
  }
  *{box-sizing:border-box;margin:0;padding:0}
  html,body{width:795px;height:1200px;overflow:hidden}
  body{font-family:"Open Sans",Arial,sans-serif;color:var(--text);background:var(--white);position:relative}

  .site-header{height:80px;position:relative;border-bottom:1px solid #eee}
  .brand{position:absolute;left:22px;top:16px;font-family:"Montserrat",Arial,sans-serif;font-weight:700;font-size:19px;line-height:22px;color:var(--ink);letter-spacing:.5px}
  .header-phone{position:absolute;right:24px;top:14px;font-size:11px;color:var(--muted)}
  .header-phone strong{color:var(--ink);font-size:13px;font-weight:600}
  .header-phone svg{vertical-align:-2px;margin-right:3px}
  .main-nav{position:absolute;right:16px;top:40px;display:flex;gap:4px}
  .main-nav a{font-size:10px;color:var(--ink);text-decoration:none;padding:7px 14px;letter-spacing:.4px}
  .main-nav a.active{border:1px solid var(--line)}

  .hero{position:absolute;top:80px;left:0;width:795px;height:398px;background:linear-gradient(180deg,#8e8e8e 0%,#6a6a6a 40%,#4c4c4c 75%,#3a3a3a 100%)}
  .hero-content{position:absolute;left:0;right:0;top:128px;text-align:center;color:var(--white)}
  .hero-title{font-weight:700;font-size:33px;letter-spacing:.5px;margin-bottom:6px}
  .hero-sub{font-size:19px;font-weight:400;line-height:26px;width:520px;margin:0 auto}
  .btn-dark{display:inline-block;margin-top:14px;background:#2c2c2c;color:var(--white);font-size:9px;letter-spacing:1px;padding:7px 14px;border:1px solid #555}
  .hero-arrow{position:absolute;top:185px}
  .hero-arrow.prev{left:34px}.hero-arrow.next{right:34px}

  .about{position:absolute;top:478px;left:0;width:795px;height:198px;text-align:center}
  .section-title{display:flex;align-items:center;justify-content:center;gap:18px;font-size:21px;font-weight:400;color:#444;letter-spacing:.5px;margin-top:34px}
  .section-title::before,.section-title::after{content:"";width:110px;height:1px;background:var(--line)}
  .about p{width:670px;margin:18px auto 0;font-size:9.5px;line-height:15px;color:var(--text)}
  .btn-outline{display:inline-block;margin-top:16px;font-size:8.5px;letter-spacing:1px;padding:6px 13px;border:1px solid var(--line);color:var(--ink)}

  .services{position:absolute;top:676px;left:0;width:795px;height:291px;background:var(--dark);color:var(--white);text-align:center}
  .services .section-title{color:var(--white);margin-top:34px}
  .services .section-title::before,.services .section-title::after{background:#555}
  .services .section-title b{font-weight:700}
  .service-grid{display:flex;justify-content:center;gap:36px;margin-top:24px}
  .service{width:150px}
  .service-icon{width:56px;height:56px;border-radius:50%;background:var(--white);margin:0 auto;display:flex;align-items:center;justify-content:center}
  .service h3{font-size:11px;font-weight:600;letter-spacing:.5px;margin-top:12px}
  .service p{font-size:8.5px;line-height:13px;color:#bdbdbd;margin-top:8px}
  .btn-small{display:inline-block;margin-top:10px;font-size:7.5px;letter-spacing:1px;padding:4px 10px;border:1px solid #777;color:var(--white)}

  .updates{position:absolute;top:967px;left:0;width:795px;height:198px;display:flex;padding:0 22px;gap:34px}
  .column{flex:1;padding-top:28px}
  .column-head{display:flex;justify-content:space-between;align-items:center;font-size:19px;color:#333;margin-bottom:14px}
  .pager{font-size:16px;color:#aaa;letter-spacing:6px}
  .news-list{display:flex;gap:18px}
  .news-item{display:flex;gap:10px;flex:1}
  .news-date{text-align:center;min-width:28px}
  .news-date .day{font-size:19px;font-weight:700;color:var(--ink);line-height:20px}
  .news-date .mon{font-size:8px;color:var(--muted)}
  .news-item p{font-size:8.5px;line-height:13px}
  .read-more{font-size:9px;font-weight:600;color:var(--ink);margin-top:6px;display:block}
  .blog-card{background:var(--panel);display:flex;gap:12px;padding:12px}
  .blog-avatar{width:54px;height:54px;border-radius:50%;flex:none;background:radial-gradient(circle at 50% 40%,#d8c3b3,#a68a77)}
  .blog-card p{font-size:8.5px;line-height:13px}
  .blog-card .date{color:var(--muted);font-size:8px;margin-top:4px}

  .site-footer{position:absolute;top:1165px;left:0;width:795px;height:35px;background:var(--darker);display:flex;justify-content:space-between;align-items:center;padding:0 22px}
  .site-footer small{font-size:8px;color:#aaa}
  .social{display:flex;gap:5px}
  .social span{width:15px;height:15px;border-radius:50%;background:#ddd}
</style>
</head>
<body>

<header class="site-header">
  <div class="brand">THE COPPER LANTERN<br>PARTNERS</div>
  <div class="header-phone">
    <svg width="10" height="10" viewBox="0 0 24 24"><path fill="#888" d="M6.6 10.8a15 15 0 006.6 6.6l2.2-2.2c.3-.3.7-.4 1-.2 1.1.4 2.3.6 3.6.6.6 0 1 .4 1 1V20c0 .6-.4 1-1 1A17 17 0 013 4c0-.6.4-1 1-1h3.5c.6 0 1 .4 1 1 0 1.3.2 2.5.6 3.6.1.3 0 .7-.2 1z"/></svg>CALL US: <strong>555-014-2290</strong>
  </div>
  <nav class="main-nav">
    <a class="active">HOME</a><a>SOLUTIONS</a><a>ABOUT</a><a>CONTACT</a><a>SUPPORT</a>
  </nav>
</header>

<section class="hero" role="img" aria-label="Black and white city skyline with skyscrapers">
  <svg class="hero-arrow prev" width="12" height="20" viewBox="0 0 12 20"><path d="M10 2L2 10l8 8" fill="none" stroke="#fff" stroke-width="3"/></svg>
  <svg class="hero-arrow next" width="12" height="20" viewBox="0 0 12 20"><path d="M2 2l8 8-8 8" fill="none" stroke="#fff" stroke-width="3"/></svg>
  <div class="hero-content">
    <h1 class="hero-title">THE COPPER LANTERN PARTNERS</h1>
    <p class="hero-sub">Build digital companies around innovative concepts in partnership with corporations.</p>
    <span class="btn-dark">LEARN MORE</span>
  </div>
</section>

<section class="about">
  <h2 class="section-title">ABOUT OUR COMPANY</h2>
  <p>Copper Lantern is a young and dynamic digital technology and investment firm, which will be recognized by its ability to transform conservative corporations by co-creating innovative businesses. Copper Lantern's two founders understand the conservative corporate culture from previous executive management positions. At the same time, they have advised many successful entrepreneurs in starting their businesses.</p>
  <span class="btn-outline">LEARN MORE</span>
</section>

<section class="services">
  <h2 class="section-title">OUR&nbsp;<b>SERVICES</b></h2>
  <div class="service-grid">
    <div class="service">
      <div class="service-icon"><svg width="22" height="26" viewBox="0 0 22 26"><path d="M2 1h12l6 6v18H2z" fill="#2a2a2a"/><path d="M6 12h10M6 16h10M6 20h7" stroke="#fff" stroke-width="1.6"/></svg></div>
      <h3>NEQUE PORRO</h3>
      <p>Neque porro quisquam est qui dolorem ipsum quia dolor sit amet, consectetur adipisci velit sed.</p>
      <span class="btn-small">MORE</span>
    </div>
    <div class="service">
      <div class="service-icon"><svg width="26" height="26" viewBox="0 0 26 26"><circle cx="13" cy="13" r="12" fill="#2a2a2a"/><path d="M19 7l-4 8-8 4 4-8z" fill="#fff"/></svg></div>
      <h3>QUISQUAM EST QUI</h3>
      <p>Neque porro quisquam est qui dolorem ipsum quia dolor sit amet, consectetur adipisci velit sed.</p>
      <span class="btn-small">MORE</span>
    </div>
    <div class="service">
      <div class="service-icon"><svg width="24" height="24" viewBox="0 0 24 24"><path fill="#2a2a2a" d="M6.6 10.8a15 15 0 006.6 6.6l2.2-2.2c.3-.3.7-.4 1-.2 1.1.4 2.3.6 3.6.6.6 0 1 .4 1 1V20c0 .6-.4 1-1 1A17 17 0 013 4c0-.6.4-1 1-1h3.5c.6 0 1 .4 1 1 0 1.3.2 2.5.6 3.6.1.3 0 .7-.2 1z"/></svg></div>
      <h3>DOLOREM IPSUM</h3>
      <p>Neque porro quisquam est qui dolorem ipsum quia dolor sit amet, consectetur adipisci velit sed.</p>
      <span class="btn-small">MORE</span>
    </div>
    <div class="service">
      <div class="service-icon"><svg width="20" height="26" viewBox="0 0 20 26"><path d="M10 1a9 9 0 00-9 9c0 7 9 15 9 15s9-8 9-15a9 9 0 00-9-9z" fill="#2a2a2a"/><circle cx="10" cy="10" r="3.5" fill="#fff"/></svg></div>
      <h3>DOLOR SIT AMET</h3>
      <p>Neque porro quisquam est qui dolorem ipsum quia dolor sit amet, consectetur adipisci velit sed.</p>
      <span class="btn-small">MORE</span>
    </div>
  </div>
</section>

<section class="updates">
  <div class="column">
    <div class="column-head"><span>LATEST NEWS</span><span class="pager">‹›</span></div>
    <div class="news-list">
      <article class="news-item">
        <div class="news-date"><div class="day">20</div><div class="mon">JULY 14</div></div>
        <div><p>Lorem ipsum dolor sit amet, consectetur adipiscing elit, sed do eiusmod tempor incididunt ut labore.</p><span class="read-more">read more</span></div>
      </article>
      <article class="news-item">
        <div class="news-date"><div class="day">18</div><div class="mon">JULY 14</div></div>
        <div><p>Lorem ipsum dolor sit amet, consectetur adipiscing elit, sed do eiusmod tempor incididunt ut labore.</p><span class="read-more">read more</span></div>
      </article>
    </div>
  </div>
  <div class="column">
    <div class="column-head"><span>BLOG POST</span><span class="pager">‹›</span></div>
    <article class="blog-card">
      <div class="blog-avatar" role="img" aria-label="Author portrait photo"></div>
      <div><p>Lorem ipsum dolor sit amet, consectetur adipiscing elit, sed do eiusmod tempor incididunt ut labore et dolore magna aliqua.</p><p class="date">September 2, 2014</p></div>
    </article>
  </div>
</section>

<footer class="site-footer">
  <small>Copyright © 2014, Copper Lantern. All Rights Reserved</small>
  <div class="social"><span></span><span></span><span></span><span></span><span></span></div>
</footer>

</body>
</html>
```